New Discover Site!!

Hello everyone!
We're WanderlyTrips. A tour company which offer group excursions to places like Morocco & Portugal for young adults. We have been in the business for 10 years now and we'd like to create a new fresh look and feel design. Something clean and more modern.
We offer trips to:
1 - Weekend trips Lagos, Portugal
2 - Weekend tips to Morocco
3 - 5 day trip to the Sahara Desert in Morocco
4 - Beach day trips to Cadiz
5 - Day trip to Gibraltar
6 - Costume trips
7 - Wine Tasting day trip
8 - Fiestas de Marvela
Those are the 8 boxes we'd like to have on our home-page along with an awesome header and footer. You can take a look for our current page to see sections and the text of the sections. Once we approve a nice home page from any of you designers, we will go ahead and send you the names of all the pages we'd like you to design for us. We already have someone who will code all the pages. We just need a new design for all the pages.
You can see our logo on our Blog: http://wanderlytripsblog.example/
We like websites like:
www.Holvaro.com
www.Skarnel.com
We look forward to hear from you!!
PS:
we will need the home page and other pages.
7 pages plus 8 trip pages. The trip pages they can all look the same (design wise) obviusly diferent photos, video and content. Total 15 pages.
Page 1 - Home page
Page 2 - About us. This page can look similar to:
Page 3 - FAQs. This page can look similar to:
Page 4 - Contact us. This page can look similar to: http://www.holvaro.com/contact
Page 5 - Trip check in. This page can look similar to the Skarnel.com look for flight check in. Something clean.
Page 6 - Trip videos. This page, will have the list of all our trip videos. A line or two of the trip and the video right below.
Page 7 - Trip departure info. On this page we're going to have the information on how to get to Sevilla. Also the google map of the actual meeting point and maybe a youtube video somewhere.
Page 8 - Why travel with us.
How many trip page are we going to need?
We have 8 trips. If you can just do 1 page, then you can do the same type page for all the trips. On each trip page you must add the following content:
Trip overview
Whats included
Trip dates
Photos and a youtube video.
An example of our current lagos trip page is:
https://www.wanderlytrips.example/2001/09/beach-getaway-lagos-portugal/
You can take all the content from www.WanderlyTrips.example

```html
<!DOCTYPE html>
<html lang="en">
<head>
<meta charset="utf-8">
<title>WanderlyTrips — Group Excursions</title>
<link rel="stylesheet" href="https://fonts.googleapis.com/css2?family=Arimo:wght@400;700&family=Roboto:wght@300;400&family=Ubuntu:wght@400;500;700&family=Ubuntu+Condensed&display=swap">
<style>
:root{
  --red:#cc2a1e;
  --red-dark:#a51d14;
  --gold:#f5b70f;
  --blue:#3f81ad;
  --blue-dark:#2d6690;
  --ink:#333;
  --muted:#555;
  --footer:#3b3b3b;
  --footer-line:#575757;
  --base:#121212;
  --white:#fff;
}
*{box-sizing:border-box;margin:0;padding:0}
html,body{width:943px;height:1200px;overflow:hidden;background:var(--white)}
body{position:relative;font-family:Arimo,sans-serif;color:var(--ink)}
.abs{position:absolute}

/* header */
.brand{left:62px;top:14px;display:flex;align-items:center;gap:8px}
.brand-mark{width:22px;height:22px;border-radius:50%;background:var(--red)}
.brand-name{font-family:Ubuntu,sans-serif;font-weight:700;font-size:21px;color:#222}
.brand-tag{left:94px;top:43px;font-size:6px;letter-spacing:.3px;color:#444;font-weight:700}

.util-tab{height:24px;background:#f3f3f3;border:1px solid #ddd;border-top:0;border-radius:0 0 6px 6px;
  display:flex;align-items:center;font-size:9.5px;color:#444;padding-left:34px;gap:6px}
.util-tab .sep{color:#999}
.util-tab .social{display:flex;gap:7px;margin-left:2px}
.util-tab .social i{width:10px;height:10px;border-radius:50%;background:#e26a2c;display:block}
.util-tab .lang{margin-left:24px}
.util-top{left:506px;top:0;width:377px}
.util-top::before,.util-foot::before{content:"";position:absolute;left:-14px;top:0;width:28px;height:100%;background:inherit;transform:skewX(35deg);border-left:1px solid #ddd;z-index:-1}

.main-nav{left:299px;top:41px;width:595px;height:34px;background:linear-gradient(#4b8dba,var(--blue-dark));
  border-radius:3px 3px 0 0;display:flex;font-family:"Ubuntu Condensed",sans-serif;font-size:13px;color:var(--white)}
.main-nav a{display:flex;align-items:center;padding:0 9px;border-left:1px solid #5e9dc8;text-decoration:none;color:inherit}
.main-nav .home{width:40px;justify-content:center;border-left:0}

/* hero */
.hero{left:0;top:76px;width:943px;height:348px;background:linear-gradient(160deg,#3a6a2a 0%,#b98a4a 30%,#3fa7a6 55%,#2b8a9a 70%,#b9a07a 90%)}
.finder{left:60px;top:126px;width:222px;height:247px;background:rgba(110,70,40,.78)}
.finder-head{height:45px;background:var(--red);color:var(--white);font-family:Ubuntu,sans-serif;font-weight:500;
  font-size:23px;display:flex;align-items:center;justify-content:center}
.finder label{position:absolute;font-size:9.5px;color:#f3eee8;letter-spacing:.3px}
.field{position:absolute;height:19px;background:#f4f4f4;border:1px solid #ccc;font-size:8.5px;color:#333;padding:4px 6px}
.field .chev{position:absolute;right:2px;top:2px;width:13px;height:13px;background:#2f8fd8;border-radius:2px}
.field .cal{position:absolute;right:3px;top:3px;width:12px;height:11px;border:1px solid #c33;border-top-width:3px;background:#fff}
.show-btn{left:40px;top:211px;width:143px;height:29px;background:linear-gradient(#f05a1e,#d33b10);color:var(--white);
  font-family:Ubuntu,sans-serif;font-weight:500;font-size:17px;display:flex;align-items:center;justify-content:center}

.slide-title{left:452px;top:212px;width:439px;height:43px;background:rgba(20,20,20,.82);color:var(--gold);
  font-family:Ubuntu,sans-serif;font-weight:500;font-size:25px;display:flex;align-items:center;justify-content:center}
.slide-sub{left:425px;top:258px;width:466px;height:27px;background:var(--red);color:var(--white);
  font-family:Ubuntu,sans-serif;font-size:11px;display:flex;align-items:center;padding-left:18px}
.learn-btn{left:747px;top:293px;width:143px;height:29px;background:linear-gradient(#3d86be,#225d8e);color:var(--white);
  font-family:Ubuntu,sans-serif;font-weight:500;font-size:17px;display:flex;align-items:center;justify-content:center}
.dots{left:817px;top:387px;display:flex;gap:5px}
.dots i{width:10px;height:10px;border-radius:50%;background:#888;display:block}
.dots i:first-child{background:var(--gold)}

/* featured */
.section-title{left:60px;top:451px;font-family:Roboto,sans-serif;font-weight:300;font-size:30px;color:#2b5f88}
.title-rule{left:260px;top:472px;width:620px;border-top:1px dotted #bbb}
.tour{width:195px;height:126px;border:1px solid #ccc}
.tour .photo{position:absolute;inset:0}
.tour .caption{position:absolute;left:0;right:0;bottom:0;height:38px;background:rgba(30,30,30,.72);color:var(--white);
  font-size:12px;display:flex;align-items:center;justify-content:center;text-align:center;line-height:1.15}
.tour.active .caption{background:rgba(200,30,20,.85);text-decoration:underline}
.tour .caption.left{justify-content:flex-start;text-align:left;padding-left:15px}

/* footer */
.footer{left:0;top:791px;width:943px;height:353px;background:var(--footer)}
.util-foot{left:70px;top:791px;width:400px;padding-left:26px}
.news-title{left:60px;top:869px;font-family:Arimo,sans-serif;font-weight:700;font-size:17px;color:#eee}
.input{top:900px;height:24px;background:var(--white);border:1px solid #ccc;font-size:12px;color:#888;padding:5px 12px}
.subscribe{left:348px;top:894px;width:114px;height:33px;background:#e0262a;color:var(--white);font-family:Arimo,sans-serif;
  font-weight:700;font-size:18px;display:flex;align-items:center;justify-content:center}
.foot-links{width:183px}
.foot-links li{list-style:none;height:31px;border-bottom:2px solid #2f2f2f;box-shadow:0 1px 0 var(--footer-line);
  display:flex;align-items:center;justify-content:space-between;padding:0 6px;font-family:Ubuntu,sans-serif;font-size:11.5px;color:#b8b8b8;letter-spacing:.3px}
.foot-links li::after{content:"";border-left:5px solid #999;border-top:3px solid transparent;border-bottom:3px solid transparent}

.player{left:525px;top:858px;width:356px;height:222px;background:#000}
.player .frame{position:absolute;left:11px;top:17px;width:331px;height:163px;background:linear-gradient(120deg,#c0452a,#e9a04a 45%,#6a4530)}
.player .play{position:absolute;left:144px;top:50px;width:62px;height:62px;border-radius:50%;background:rgba(200,200,200,.85)}
.player .bar{position:absolute;left:0;bottom:0;width:356px;height:23px;background:linear-gradient(#eee,#aaa)}
.time{position:absolute;left:173px;top:5px;width:55px;height:12px;background:#111;font-size:7px;color:#ddd;padding:2px 3px}

.base{left:0;top:1144px;width:943px;height:56px;background:var(--base)}
.copyright{left:103px;top:1168px;font-size:8px;color:#999}
.base-social{left:739px;top:1158px;display:flex;gap:6px}
.base-social i{width:30px;height:27px;border:1px solid #555;background:#1c1c1c;display:flex;align-items:center;justify-content:center}
.base-social i::after{content:"";width:9px;height:9px;border-radius:50%;background:#999}
</style>
</head>
<body>

<header>
  <div class="abs brand"><span class="brand-mark"></span><span class="brand-name">WanderlyTrips</span></div>
  <div class="abs brand-tag">GO BEYOND THE ORDINARY TRIP</div>

  <div class="abs util-tab util-top">
    <span>Sign Up</span><span class="sep">|</span><span>Sign In</span><span class="sep">|</span><span>Newsletter</span><span class="sep">|</span><span>Follow us</span>
    <span class="social"><i></i><i></i><i></i><i></i></span>
    <span class="lang">Language</span>
  </div>

  <nav class="abs main-nav">
    <a class="home" href="#"><svg width="16" height="14" viewBox="0 0 16 14"><path d="M8 1 1 7h2v6h4V9h2v4h4V7h2z" fill="#f5c518"/></svg></a>
    <a href="#">About Us</a><a href="#">FAQs</a><a href="#">Contact Us</a><a href="#">Trip Check In</a>
    <a href="#">Trip Videos</a><a href="#">Trip Departure Info</a><a href="#">Why Travel With Us</a>
  </nav>
</header>

<section>
  <div class="abs hero" role="img" aria-label="Golden sea cliffs and a wooden stairway down to a turquoise cove in Lagos, Portugal"></div>

  <form class="abs finder">
    <div class="finder-head">Find A Tour</div>
    <label style="left:22px;top:58px">Travel area:</label>
    <div class="field" style="left:22px;top:74px;width:178px">Please select<span class="chev"></span></div>
    <label style="left:22px;top:103px">Start date:</label>
    <label style="left:114px;top:103px">Departure Date:</label>
    <div class="field" style="left:22px;top:119px;width:83px">Fri 19 Abr 13<span class="cal"></span></div>
    <div class="field" style="left:114px;top:119px;width:83px">Sun 21 Abr 13<span class="cal"></span></div>
    <label style="left:22px;top:148px">Budget</label>
    <label style="left:114px;top:148px">Party Size:</label>
    <div class="field" style="left:22px;top:164px;width:83px">any</div>
    <div class="field" style="left:114px;top:164px;width:83px">1<span class="chev"></span></div>
    <div class="abs show-btn">Show Tours »</div>
  </form>

  <h2 class="abs slide-title">Beach Gateway to Lagos, Portugal</h2>
  <p class="abs slide-sub">At just a stone´s throw away, Lagos is the perfect destination for that weekend beach...</p>
  <div class="abs learn-btn">Learn More »</div>
  <div class="abs dots"><i></i><i></i><i></i><i></i></div>
</section>

<section>
  <h2 class="abs section-title">Featured Tours</h2>
  <div class="abs title-rule"></div>

  <div class="abs tour active" style="left:60px;top:498px">
    <div class="photo" role="img" aria-label="Lagos coastline at dusk" style="background:linear-gradient(#1c2a44,#3a3a30 60%,#6a5a40)"></div>
    <div class="caption left">Weekend trips Lagos, Portugal</div></div>
  <div class="abs tour" style="left:269px;top:498px">
    <div class="photo" role="img" aria-label="Red rock arch over a Moroccan beach" style="background:linear-gradient(#8a2a10,#d8682a 55%,#7a3a1a)"></div>
    <div class="caption">Weekend trips to Morocco</div></div>
  <div class="abs tour" style="left:478px;top:498px">
    <div class="photo" role="img" aria-label="Camel caravan crossing Sahara dunes" style="background:linear-gradient(#f0e6d4,#d79a4a 45%,#b86a2a)"></div>
    <div class="caption left">5 day trip to the Sahara Desert<br>in Morocco</div></div>
  <div class="abs tour" style="left:687px;top:498px">
    <div class="photo" role="img" aria-label="Cadiz cathedral and seafront" style="background:linear-gradient(#1f5bb0,#6aa0d8 40%,#c8b890 65%,#6a7a88)"></div>
    <div class="caption">Beach day trips to Cadiz</div></div>

  <div class="abs tour" style="left:60px;top:639px">
    <div class="photo" role="img" aria-label="Rock of Gibraltar above the sea" style="background:linear-gradient(#cfe0ec,#8aa0a8 40%,#2f6c8a 80%)"></div>
    <div class="caption">Day trip to Gibraltar</div></div>
  <div class="abs tour" style="left:269px;top:639px">
    <div class="photo" role="img" aria-label="Market square with costumed performers" style="background:linear-gradient(#d8c8b8,#a24a3a 55%,#6a3a30)"></div>
    <div class="caption">Costume Trips</div></div>
  <div class="abs tour" style="left:478px;top:639px">
    <div class="photo" role="img" aria-label="Two glasses of red wine over a vineyard" style="background:linear-gradient(#7a8a6a,#5a4a3a 60%,#3a2020)"></div>
    <div class="caption">Wine Tasting day trip</div></div>
  <div class="abs tour" style="left:687px;top:639px">
    <div class="photo" role="img" aria-label="Colourful carnival parade figures" style="background:linear-gradient(#d8d0c0,#b04a2a 50%,#3a3a5a)"></div>
    <div class="caption">Fiestas de Marvela</div></div>
</section>

<footer>
  <div class="abs footer"></div>
  <div class="abs util-tab util-foot">
    <span>Sign Up</span><span class="sep">|</span><span>Sign In</span><span class="sep">|</span><span>Newsletter</span><span class="sep">|</span><span>Follow us</span>
    <span class="social"><i></i><i></i><i></i><i></i></span>
    <span class="lang">Language</span>
  </div>

  <h3 class="abs news-title">Join our Newsletter</h3>
  <div class="abs input" style="left:60px;width:135px">Name:</div>
  <div class="abs input" style="left:202px;width:136px">Email:</div>
  <div class="abs subscribe">Subscribe</div>

  <ul class="abs foot-links" style="left:60px;top:960px"><li>Home</li><li>About Us</li><li>FAQs</li><li>Contact Us</li></ul>
  <ul class="abs foot-links" style="left:286px;top:960px"><li>Trip Check In</li><li>Trip Videos</li><li>Trip Departure Info</li><li>Why Travel with Us</li></ul>

  <div class="abs player">
    <div class="frame" role="img" aria-label="Video still of travellers on a trip"></div>
    <div class="play"><svg width="62" height="62" viewBox="0 0 62 62"><path d="M24 18v26l21-13z" fill="#222"/></svg></div>
    <div class="bar">
      <svg width="356" height="23" viewBox="0 0 356 23">
        <rect x="8" y="6" width="3" height="11" fill="#444"/><rect x="13" y="6" width="3" height="11" fill="#444"/>
        <path d="M32 6v11M43 6l-9 5.5 9 5.5z" stroke="#444" fill="#444"/>
        <rect x="58" y="10" width="110" height="3" rx="1.5" fill="#555"/><circle cx="62" cy="11.5" r="4" fill="#ddd" stroke="#555"/>
        <rect x="240" y="10" width="40" height="3" fill="#555"/>
        <path d="M283 8h3l4-3v13l-4-3h-3z" fill="#444"/>
        <rect x="313" y="6" width="14" height="10" fill="none" stroke="#444"/><rect x="332" y="6" width="16" height="10" fill="none" stroke="#444"/>
      </svg>
      <div class="time">00:00 / <span style="color:#e33">01:47</span></div>
    </div>
  </div>

  <div class="abs base"></div>
  <p class="abs copyright">Copyright © 2013 WanderlyTrips. All Rights Reserved.</p>
  <div class="abs base-social"><i></i><i></i><i></i><i></i></div>
</footer>

</body>
</html>
```